Award winning photographer needs a website.

I need a Wordpress website that showcases my photos. I want them arranged via category, which might be a specific place or a theme. Here are categories I am thinking of:
1. Yarra Valley and Ranges
2. East coast Tasmania
3. Landscapes
4. Seascapes
5. Urban
6. Nepal
7. Macro
I need to be able to upload and download the photos myself. Currently, there is no need for this site to have an ecommerce component. I would like a blog page where I can post about my photographic adventures and maybe add some short videos of me on my way to the shoot, or of the people I meet. I also want to have it so that each photo has a title and if people click on a photo they can read a story about how I came to shoot it etc. There will also be my contact details and how to purchase a print which will happen through other communications. Like i mentioned, no e commerce at this point. I would like a page for awards as I have several. Here are some URLs of sites I like to give you some idea of what I'm looking at:

https://www.lumavesk.com/
https://darbyquillenphotography.com/
https://www.marisolvexphotography.com/

I can upload some images for you to start putting together someting if that hepls

Photography

Coded - Design and coding required

5+ page

Sans Serif

• Multiple pages to display photos in different categories

```html
<!DOCTYPE html>
<html lang="en">
<head>
<meta charset="utf-8">
<title>Ellis Brandwater — Award Winning Photographer</title>
<link rel="stylesheet" href="https://fonts.googleapis.com/css2?family=Jost:wght@400;500;600&display=swap">
<style>
  :root {
    --ink: #1c1c1c;
    --white: #ffffff;
    --muted: #5a5a5a;
    --panel: #1d1915;
    --hero-top: #2b2b2b;
    --hero-mid: #6e6e6e;
    --hero-low: #3a3a3a;
    --icon-bg: #3a3a3a;
  }
  * { box-sizing: border-box; margin: 0; padding: 0; }
  html, body { width: 1200px; height: 2280px; overflow: hidden; background: var(--white); }
  body { font-family: "Jost", "Futura", sans-serif; color: var(--ink); position: relative; }

  .hero {
    position: absolute; left: 0; top: 0; width: 1200px; height: 600px;
    background: linear-gradient(180deg, var(--hero-top) 0%, #4a4a4a 30%, var(--hero-mid) 55%, var(--hero-low) 100%);
  }
  .brand {
    position: absolute; top: 58px; width: 100%; text-align: center;
    color: var(--white); font-size: 24px; font-weight: 500; letter-spacing: 2px;
  }
  .headline {
    position: absolute; top: 150px; width: 100%; text-align: center;
    color: var(--white); font-size: 60px; font-weight: 500; line-height: 1.08; letter-spacing: 1px;
  }
  .filters {
    position: absolute; top: 350px; left: 0; width: 100%;
    display: flex; justify-content: center; align-items: center; gap: 40px;
    list-style: none;
  }
  .filters li { color: var(--white); font-size: 12px; font-weight: 500; letter-spacing: 0.5px; text-transform: uppercase; }
  .filters li.active { background: var(--white); color: var(--ink); padding: 7px 14px; }

  .photo { position: absolute; }
  .intro {
    position: absolute; left: 437px; top: 432px; width: 326px; height: 448px;
    background: var(--panel); color: var(--white); text-align: center; padding: 60px 34px 0;
  }
  .intro h2 { font-size: 32px; font-weight: 600; margin-bottom: 26px; }
  .intro p { font-size: 16px; line-height: 1.45; margin-bottom: 34px; }
  .intro a { color: var(--white); text-decoration: none; font-size: 16px; font-weight: 600; }

  .footer-name {
    position: absolute; top: 1992px; width: 100%; text-align: center;
    font-size: 36px; font-weight: 500; letter-spacing: 1px;
  }
  .contacts { position: absolute; top: 2100px; left: 0; width: 100%; }
  .contact { position: absolute; display: flex; align-items: center; gap: 20px; }
  .contact .icon {
    width: 46px; height: 46px; border-radius: 50%; background: var(--icon-bg);
    display: flex; align-items: center; justify-content: center;
  }
  .contact .label { font-size: 15px; line-height: 1.4; }
  .contact .value { font-size: 15px; color: var(--muted); line-height: 1.4; }
  .copyright {
    position: absolute; top: 2210px; width: 100%; text-align: center;
    font-size: 15px; color: var(--muted);
  }
</style>
</head>
<body>
  <header class="hero">
    <div class="brand">ELLIS BRANDWATER</div>
    <h1 class="headline">AWARD WINNING<br>PHOTOGRAPHER</h1>
    <ul class="filters">
      <li class="active">All</li>
      <li>Yarra Valley and Ranges</li>
      <li>East Coast Tasmania</li>
      <li>Landscapes</li>
      <li>Seascapes</li>
      <li>Urban</li>
      <li>Nepal</li>
      <li>Macro</li>
    </ul>
  </header>

  <main class="gallery">
    <div class="photo" role="img" aria-label="Sunset over calm water with orange sky" style="left:100px;top:432px;width:325px;height:240px;background:linear-gradient(180deg,#5b6a8a 0%,#d88a4a 55%,#2a2a38 100%);"></div>
    <section class="intro">
      <h2>Lorem Ipsum</h2>
      <p>Lorem ipsum dolor sit amet, consectetur adipiscing elit, sed do eiusmod tempor incididunt ut labore et dolore magna aliqua. Quis ipsum suspendisse ultrices gravida. Risus commodo viverra maecenas accumsan lacus vel facilisis.</p>
      <a href="#">Learn More</a>
    </section>
    <div class="photo" role="img" aria-label="Winding road under a pink dusk sky" style="left:775px;top:432px;width:325px;height:240px;background:linear-gradient(180deg,#4e5a7e 0%,#b27a9a 50%,#3b4a3e 100%);"></div>

    <div class="photo" role="img" aria-label="Green coastal hills and ocean" style="left:100px;top:688px;width:325px;height:224px;background:linear-gradient(180deg,#b9c8cf 0%,#5f8a5a 55%,#2f4a32 100%);"></div>
    <div class="photo" role="img" aria-label="Long exposure of blue sea" style="left:775px;top:688px;width:325px;height:224px;background:linear-gradient(180deg,#1e3a6a 0%,#3a6aa0 50%,#0f2244 100%);"></div>

    <div class="photo" role="img" aria-label="Golden sunset beneath a pier" style="left:100px;top:928px;width:325px;height:480px;background:linear-gradient(180deg,#4a3a3a 0%,#c9782a 45%,#f0a540 60%,#2a1d14 100%);"></div>
    <div class="photo" role="img" aria-label="Orange lichen rocks at sunrise" style="left:437px;top:928px;width:326px;height:232px;background:linear-gradient(180deg,#e0a060 0%,#b85a2a 55%,#3a2a24 100%);"></div>
    <div class="photo" role="img" aria-label="Rock stack in misty blue sea" style="left:437px;top:1176px;width:326px;height:232px;background:linear-gradient(180deg,#9aa6c0 0%,#6c7898 55%,#2e3444 100%);"></div>
    <div class="photo" role="img" aria-label="Black and white bridge at night" style="left:775px;top:928px;width:325px;height:480px;background:linear-gradient(180deg,#2a2a2a 0%,#7a7a7a 45%,#d0d0d0 65%,#3a3a3a 100%);"></div>

    <div class="photo" role="img" aria-label="Figures silhouetted against a pale sky" style="left:100px;top:1424px;width:325px;height:224px;background:linear-gradient(180deg,#e8dcb8 0%,#b8a880 55%,#2a2a2a 100%);"></div>
    <div class="photo" role="img" aria-label="Sunset over a valley" style="left:100px;top:1664px;width:325px;height:224px;background:linear-gradient(180deg,#3a4a6a 0%,#e08a3a 50%,#4a3a5a 100%);"></div>
    <div class="photo" role="img" aria-label="Misty cliffs and forest" style="left:437px;top:1424px;width:326px;height:464px;background:linear-gradient(180deg,#c8c8c8 0%,#8a8a82 45%,#3a3e34 100%);"></div>
    <div class="photo" role="img" aria-label="City lights by night" style="left:775px;top:1424px;width:325px;height:224px;background:linear-gradient(180deg,#1a2040 0%,#4a3a5a 50%,#d89a40 80%,#1a1a22 100%);"></div>
    <div class="photo" role="img" aria-label="Country road under a stormy sky" style="left:775px;top:1664px;width:325px;height:224px;background:linear-gradient(180deg,#4a5a7a 0%,#b89a6a 55%,#6a4a2a 100%);"></div>
  </main>

  <footer>
    <div class="footer-name">ELLIS BRANDWATER</div>
    <div class="contacts">
      <div class="contact" style="left:200px;">
        <span class="icon"><svg width="20" height="20" viewBox="0 0 24 24"><path d="M12 2a7 7 0 0 0-7 7c0 5 7 13 7 13s7-8 7-13a7 7 0 0 0-7-7zm0 9.5a2.5 2.5 0 1 1 0-5 2.5 2.5 0 0 1 0 5z" fill="#fff"/></svg></span>
        <div><div class="label">Location</div><div class="value">TBC United State</div></div>
      </div>
      <div class="contact" style="left:440px;">
        <span class="icon"><svg width="20" height="20" viewBox="0 0 24 24"><path d="M6.6 10.8a15 15 0 0 0 6.6 6.6l2.2-2.2c.3-.3.7-.4 1-.2 1.1.4 2.3.6 3.6.6.6 0 1 .4 1 1V20c0 .6-.4 1-1 1A17 17 0 0 1 3 4c0-.6.4-1 1-1h3.5c.6 0 1 .4 1 1 0 1.3.2 2.5.6 3.6.1.3 0 .7-.2 1z" fill="#fff"/></svg></span>
        <div><div class="label">Phone</div><div class="value">+1 888 888 8888</div></div>
      </div>
      <div class="contact" style="left:690px;">
        <span class="icon"><svg width="20" height="20" viewBox="0 0 24 24"><path d="M3 5h18v14H3z" fill="#fff"/><path d="M3 5l9 7 9-7" fill="none" stroke="#3a3a3a" stroke-width="1.6"/></svg></span>
        <div><div class="label">Email</div><div class="value">hello@ellisbrandwater.com</div></div>
      </div>
    </div>
    <div class="copyright">©Copyrights 2022 Ellis Brandwater &nbsp; | &nbsp; All Rights Reserved</div>
  </footer>
</body>
</html>
```